Reputable business cards for Diplom Kauffrau, Privat und Geschäftslich

The business cards should be reputable, valuable and elegant in order to be able to use them for business. The design should also include a sophistication that is conspicuous. This could be a picture, an ornament, a sublime print or a kind of logo of the initials of my name "MK". The font should be clear and legible.
Target Market(s)
Business contacts, friends and acquaintances
Contact Information for Business Card
Diplom-Kauffrau Marietta Kuhnle
Lindenhofweg 37 50391 Frechen
Mobil +49 170 418 29 57
e-mail marietta.kuhnle@postfeld.de
Font styles to use
Colors
Designer to choose colors to be used in the design.
Requirements
Must have
- Clear and easy to read font My name in larger font than the other information Visual conspicuity / specificity
Nice to have
- Different colors
Should not have
- Ornate font, playful

```html
<!DOCTYPE html>
<html lang="de">
<head>
<meta charset="utf-8">
<title>Marietta Kuhnle – Visitenkarte</title>
<link rel="stylesheet" href="https://fonts.googleapis.com/css2?family=Didact+Gothic&family=Poppins:wght@600&display=swap">
<style>
  :root {
    --stage: #1d1d1d;
    --card-light: #ffffff;
    --card-vein: #e6e6e8;
    --name-blue: #4450a6;
    --title-red: #e3262d;
    --text-dark: #141414;
    --mark-ring: #8a6fd0;
  }
  * { margin: 0; padding: 0; box-sizing: border-box; }
  html, body {
    width: 1200px; height: 1200px; overflow: hidden;
    background: var(--stage);
  }
  .stage {
    width: 1200px; height: 1200px;
    display: flex; align-items: center; justify-content: center;
  }
  .business-card {
    position: relative;
    width: 1000px; height: 572px;
    border-radius: 34px;
    overflow: hidden;
    text-align: center;
  }
  .card-marble {
    position: absolute; inset: 0;
    background:
      linear-gradient(155deg, transparent 30%, var(--card-vein) 42%, transparent 54%),
      linear-gradient(25deg, transparent 55%, var(--card-vein) 68%, transparent 80%),
      radial-gradient(circle at 50% 45%, var(--card-light) 35%, #f1f1f2 100%);
  }
  .card-content {
    position: relative;
    padding-top: 42px;
    display: flex; flex-direction: column; align-items: center;
  }
  .monogram {
    width: 190px; height: 190px;
    border-radius: 50%;
    border: 5px solid var(--mark-ring);
    display: flex; align-items: center; justify-content: center;
    font-family: "Didact Gothic", sans-serif;
    font-size: 92px;
    color: var(--name-blue);
    letter-spacing: 2px;
  }
  .holder-name {
    margin-top: 26px;
    font-family: "Poppins", sans-serif;
    font-weight: 600;
    font-size: 50px;
    letter-spacing: 2px;
    color: var(--name-blue);
    line-height: 1.05;
  }
  .holder-title {
    font-family: "Didact Gothic", sans-serif;
    font-size: 32px;
    letter-spacing: 1.5px;
    color: var(--title-red);
    line-height: 1.2;
  }
  .contact-list {
    margin-top: 14px;
    list-style: none;
    font-family: "Didact Gothic", sans-serif;
    font-size: 25px;
    color: var(--text-dark);
    line-height: 1.38;
  }
</style>
</head>
<body>
  <main class="stage">
    <article class="business-card">
      <div class="card-marble" role="img" aria-label="Weiße Marmorstruktur mit hellgrauen Adern"></div>
      <div class="card-content">
        <div class="monogram">MK</div>
        <h1 class="holder-name">MARIETTA KUHNLE</h1>
        <p class="holder-title">DIPLOM-KAUFFRAU</p>
        <ul class="contact-list">
          <li>Address : Lindenhofweg 37 50391 Frechen</li>
          <li>Phone : +49 170 418 29 57</li>
          <li>Email : marietta.kuhnle@postfeld.de</li>
        </ul>
      </div>
    </article>
  </main>
</body>
</html>
```